Company or website name
- Copperfield Staff Bulletins
- Links to the website
- I 'breathe fresh life' into office workplaces with these inspirational wellbeing newsletters! =)
- Other Facts

```html
<!DOCTYPE html>
<html lang="en">
<head>
<meta charset="utf-8">
<title>Employee Well Being Program – Masthead Options</title>
<link rel="stylesheet" href="https://fonts.googleapis.com/css2?family=Great+Vibes&family=Arimo&display=swap">
<style>
  :root {
    --page: #ffffff;
    --lilac: #9a9cf0;
    --mint: #96e2d6;
    --rule-green: #33c433;
    --deep-blue: #0660dc;
    --bright-blue: #2fb4ff;
    --sky-top: #2f6fd8;
    --sky-low: #9cc0ef;
    --title-white: #ffffff;
    --title-outline: #000000;
    --well-green: #7cf27c;
    --well-outline: #0d5a12;
    --issue-yellow: #f4f02a;
    --ornament: #000000;
  }
  html, body {
    margin: 0;
    padding: 0;
    width: 1200px;
    height: 1164px;
    overflow: hidden;
    background: var(--page);
  }
  .sheet {
    position: relative;
    width: 1200px;
    height: 1164px;
  }
  .masthead {
    position: absolute;
    left: 0;
    width: 1200px;
    display: block;
  }
  .masthead--lilac { top: 0; height: 272px; }
  .masthead--blue-double { top: 290px; height: 265px; }
  .masthead--blue-single { top: 578px; height: 270px; }
  .masthead--sky { top: 867px; height: 266px; }
  .title {
    font-family: "Great Vibes", cursive;
    font-size: 96px;
    paint-order: stroke fill;
    stroke-linejoin: round;
  }
  .title__plain { fill: var(--title-white); stroke: var(--title-outline); stroke-width: 2.4px; }
  .title__accent { fill: var(--well-green); stroke: var(--well-outline); stroke-width: 2.4px; }
  .issue {
    font-family: "Arimo", Arial, sans-serif;
    font-size: 27px;
    fill: var(--issue-yellow);
    white-space: pre;
  }
</style>
</head>
<body>
<main class="sheet">

  <!-- Option 1: lilac to mint with green rule -->
  <svg class="masthead masthead--lilac" viewBox="0 0 1200 272" xmlns="http://www.w3.org/2000/svg">
    <defs>
      <linearGradient id="lilac-fade" x1="0" y1="0" x2="0" y2="1">
        <stop offset="0" stop-color="var(--lilac)"/>
        <stop offset="1" stop-color="var(--mint)"/>
      </linearGradient>
      <radialGradient id="ornament-shade" cx="0.5" cy="0.5" r="0.5">
        <stop offset="0" stop-color="var(--ornament)" stop-opacity="0.45"/>
        <stop offset="1" stop-color="var(--ornament)" stop-opacity="0"/>
      </radialGradient>
    </defs>
    <rect width="1200" height="260" fill="url(#lilac-fade)"/>
    <rect y="260" width="1200" height="12" fill="var(--rule-green)"/>
    <rect class="ornament" x="495" y="0" width="210" height="75" rx="30" fill="url(#ornament-shade)" role="img" aria-label="Decorative scroll flourish"/>
    <text class="issue" x="1178" y="32" text-anchor="end">Issue:  12  2009</text>
    <text class="title" x="22" y="168" textLength="1163" lengthAdjust="spacingAndGlyphs"><tspan class="title__plain">Employee </tspan><tspan class="title__accent">Well Being</tspan><tspan class="title__plain"> Program</tspan></text>
  </svg>

  <!-- Option 2: bright blue with flourishes above and below -->
  <svg class="masthead masthead--blue-double" viewBox="0 0 1200 265" xmlns="http://www.w3.org/2000/svg">
    <defs>
      <radialGradient id="blue-glow-a" cx="0.5" cy="0.5" r="0.75" gradientTransform="translate(0.5 0.5) scale(1 0.6) translate(-0.5 -0.5)">
        <stop offset="0" stop-color="var(--bright-blue)"/>
        <stop offset="1" stop-color="var(--deep-blue)"/>
      </radialGradient>
      <radialGradient id="ornament-shade-b" cx="0.5" cy="0.5" r="0.5">
        <stop offset="0" stop-color="var(--ornament)" stop-opacity="0.45"/>
        <stop offset="1" stop-color="var(--ornament)" stop-opacity="0"/>
      </radialGradient>
    </defs>
    <rect width="1200" height="265" fill="url(#blue-glow-a)"/>
    <rect class="ornament" x="487" y="10" width="225" height="75" rx="30" fill="url(#ornament-shade-b)" role="img" aria-label="Decorative scroll flourish"/>
    <rect class="ornament" x="487" y="185" width="225" height="75" rx="30" fill="url(#ornament-shade-b)" role="img" aria-label="Decorative scroll flourish, mirrored"/>
    <text class="issue" x="1163" y="40" text-anchor="end">Issue:  12  2009</text>
    <text class="title" x="22" y="160" textLength="1156" lengthAdjust="spacingAndGlyphs"><tspan class="title__plain">Employee </tspan><tspan class="title__accent">Well Being</tspan><tspan class="title__plain"> Program</tspan></text>
  </svg>

  <!-- Option 3: bright blue with single flourish -->
  <svg class="masthead masthead--blue-single" viewBox="0 0 1200 270" xmlns="http://www.w3.org/2000/svg">
    <defs>
      <radialGradient id="blue-glow-b" cx="0.5" cy="0.5" r="0.75" gradientTransform="translate(0.5 0.5) scale(1 0.6) translate(-0.5 -0.5)">
        <stop offset="0" stop-color="var(--bright-blue)"/>
        <stop offset="1" stop-color="var(--deep-blue)"/>
      </radialGradient>
      <radialGradient id="ornament-shade-c" cx="0.5" cy="0.5" r="0.5">
        <stop offset="0" stop-color="var(--ornament)" stop-opacity="0.45"/>
        <stop offset="1" stop-color="var(--ornament)" stop-opacity="0"/>
      </radialGradient>
    </defs>
    <rect width="1200" height="270" fill="url(#blue-glow-b)"/>
    <rect class="ornament" x="472" y="12" width="278" height="72" rx="30" fill="url(#ornament-shade-c)" role="img" aria-label="Decorative scroll flourish"/>
    <text class="issue" x="1148" y="42" text-anchor="end">Issue:  12  2009</text>
    <text class="title" x="15" y="170" textLength="1148" lengthAdjust="spacingAndGlyphs"><tspan class="title__plain">Employee </tspan><tspan class="title__accent">Well Being</tspan><tspan class="title__plain"> Program</tspan></text>
  </svg>

  <!-- Option 4: cloudy sky -->
  <svg class="masthead masthead--sky" viewBox="0 0 1200 266" xmlns="http://www.w3.org/2000/svg">
    <defs>
      <linearGradient id="sky-fade" x1="0" y1="0" x2="0.3" y2="1">
        <stop offset="0" stop-color="var(--sky-top)"/>
        <stop offset="1" stop-color="var(--sky-low)"/>
      </linearGradient>
    </defs>
    <rect class="sky" width="1200" height="266" fill="url(#sky-fade)" role="img" aria-label="Blue sky with soft white clouds"/>
    <text class="issue" x="1163" y="42" text-anchor="end">Issue:  12  2009</text>
    <text class="title" x="27" y="162" textLength="1150" lengthAdjust="spacingAndGlyphs"><tspan class="title__plain">Employee </tspan><tspan class="title__accent">Well Being</tspan><tspan class="title__plain"> Program</tspan></text>
  </svg>

</main>
</body>
</html>
```